Design New Business Card, Envelope and Letter Head !

We need a stationery design for our newly developed logo! We need professional classic look.

Front of the Card:
Logo on the left hand side

Personal Detail in the right hand side
i.e. Name,
Title
Office:
Cell:
Fax:
email:

www.corvelmortgage.example

Color Scheme should match our logo.

Back Side of the Card:

Logo again with Green back ground or off gray back ground ( Note: Color has to be from logo)

and below message. Again, font size and color should come from logo.

" Manifest your trust in us through the gift of your referrals. We won't let you down."
Updates

Dear Designers;

We have updates few info which we missed earlier. Please include those words in the logo and resubmit your designs for consideration.  We are looking for very professional and classic look. Thanks for your great creation. I have changed the payment options. Please have a look and best of luck.

Tobin

Dear All Designers:

For address; please use following address:

" 4719 Copper Glen Ln, San Ramon, CA 94583 " 
Please do not use the address in the website. We would like to give business card with option of calling us is the top priority then email then eFax. Please make sure Put " eFax" in the business card. 

Reason: Since I have updated some information per requirements, I would like to give enough time for the great design work.

Just a note to all designers:

"Equal Opportunity Lender" Sign has to be in back  of the card  in a small image. I would say it has to be "inconspicuous". Let's put the NMLS # and CalBRE # in front side. Let's organise the information follow very elegant and professional.

Requirements
Must have
• We must need following Words in the business card

CalBRE License #

NMLS #

And the logo of " Equal Housing Lender ". Please see the logo attached.

Please put these words or logo represents above at the right location of the card.

```html
<!DOCTYPE html>
<html lang="en">
<head>
<meta charset="utf-8">
<title>Brisvane Home Loans Stationery</title>
<link rel="stylesheet" href="https://fonts.googleapis.com/css2?family=Libre+Baskerville:wght@400;700&display=swap">
<style>
  :root{
    --slate:#5b6167;
    --green:#4dae3c;
    --ink:#555a60;
    --paper:#ffffff;
    --backdrop:#e4e5e6;
  }
  *{box-sizing:border-box;margin:0;padding:0}
  html,body{width:1000px;height:1200px;overflow:hidden}
  body{background:var(--backdrop);font-family:'Libre Baskerville',serif;color:var(--ink);position:relative}
  .sheet{position:absolute;background:var(--paper);box-shadow:0 2px 6px rgba(0,0,0,.25);overflow:hidden}
  .brand{display:flex;align-items:center;gap:8px;color:var(--slate);font-family:'Libre Baskerville',serif;font-weight:400;white-space:nowrap;line-height:1}
  .brand-dot{display:inline-block;background:var(--green);flex:none}
  .contact{display:flex;align-items:center;gap:5px;font-size:10px;letter-spacing:1px;color:var(--ink);white-space:nowrap;line-height:1.2}
  .contact svg{width:10px;height:10px;fill:var(--green);flex:none}
  .abs{position:absolute}

  /* Letterhead */
  .letterhead{left:20px;top:20px;width:960px;height:300px}
  .letterhead .top-band{left:0;top:0;width:100%;height:26px;background:var(--slate)}
  .letterhead .top-rule{left:0;top:32px;width:100%;height:5px;background:var(--green)}
  .letterhead .brand{left:432px;top:122px;font-size:24px}
  .letterhead .brand-dot{width:11px;height:11px}

  /* Cards */
  .card{top:357px;width:400px;height:268px}
  .card-front{left:88px}
  .card-front .brand{left:14px;top:94px;font-size:19px}
  .card-front .brand-dot{width:9px;height:9px}
  .card-front .person{left:22px;top:172px}
  .person-name{font-size:13px;font-weight:700;letter-spacing:1.2px;color:#3f4449}
  .person-title{font-size:9px;letter-spacing:.8px;margin-top:4px;color:#777}
  .card-front .details{left:188px;top:140px;display:flex;flex-direction:column;gap:4px}
  .card-front .contact{font-size:8.5px}
  .card-front .contact.addr{align-items:flex-start}
  .card-front .front-rule{left:0;bottom:28px;width:100%;height:6px;background:var(--green)}
  .card-front .front-band{left:0;bottom:0;width:100%;height:24px;background:var(--slate)}

  .card-back{left:514px;background:var(--slate)}
  .card-back .site{left:0;top:16px;width:100%;text-align:center;font-size:9px;letter-spacing:.8px;color:#fff}
  .card-back .brand{left:50%;top:120px;transform:translateX(-50%);font-size:19px;color:#fff}
  .card-back .brand-dot{width:9px;height:9px;background:#fff}
  .card-back .message{left:0;top:198px;width:100%;text-align:center;font-size:9.5px;line-height:1.45;color:#fff}
  .card-back .back-rule{left:0;bottom:26px;width:100%;height:6px;background:#fff}
  .card-back .back-band{left:0;bottom:0;width:100%;height:26px;background:var(--green)}

  /* Envelope */
  .envelope{left:20px;top:655px;width:960px;height:525px}
  .envelope .brand{left:282px;top:80px;font-size:30px}
  .envelope .brand-dot{width:13px;height:13px}
  .envelope .bottom-rule{left:0;bottom:66px;width:100%;height:6px;background:var(--green)}
  .envelope .bottom-band{left:0;bottom:0;width:100%;height:60px;background:var(--slate)}
</style>
</head>
<body>

<svg width="0" height="0" style="position:absolute" aria-hidden="true">
  <defs>
    <symbol id="icon-pin" viewBox="0 0 10 10"><path d="M5 0C3 0 1.6 1.5 1.6 3.4 1.6 6 5 10 5 10s3.4-4 3.4-6.6C8.4 1.5 7 0 5 0zm0 4.8a1.4 1.4 0 1 1 0-2.8 1.4 1.4 0 0 1 0 2.8z"/></symbol>
    <symbol id="icon-phone" viewBox="0 0 10 10"><circle cx="5" cy="5" r="5"/><path d="M3.2 2.4l1 .9-.4.8c.4.8 1 1.4 1.8 1.8l.8-.4.9 1-.6.9C4.9 7.2 2.8 5.1 2.6 3z" fill="#fff"/></symbol>
    <symbol id="icon-mobile" viewBox="0 0 10 10"><path d="M2.8 0h4.4c.4 0 .8.4.8.8v8.4c0 .4-.4.8-.8.8H2.8c-.4 0-.8-.4-.8-.8V.8c0-.4.4-.8.8-.8zM3 1.2v6.6h4V1.2z"/></symbol>
    <symbol id="icon-fax" viewBox="0 0 10 10"><path d="M2.5 0h5v2.5h-5zM1 3h8c.5 0 1 .4 1 1v3H8V5.5H2V7H0V4c0-.6.5-1 1-1zM2.5 6h5v4h-5z"/></symbol>
    <symbol id="icon-mail" viewBox="0 0 10 10"><path d="M0 2h10v6H0zM.6 2.4L5 5.6l4.4-3.2"/></symbol>
  </defs>
</svg>

<!-- Letterhead -->
<section class="sheet letterhead" aria-label="Letterhead">
  <div class="abs top-band"></div>
  <div class="abs top-rule"></div>
  <div class="abs brand"><span class="brand-dot"></span>Brisvane Home Loans</div>
  <div class="abs contact" style="left:180px;top:140px"><svg><use href="#icon-pin"/></svg>xxx xxxxxxx xxxxx</div>
  <div class="abs contact" style="left:195px;top:162px">xxxxxxxxx, xxxxxxxx xxxxx xxx</div>
  <div class="abs contact" style="left:410px;top:178px"><svg><use href="#icon-phone"/></svg>(xxx) xxx xxxx</div>
  <div class="abs contact" style="left:535px;top:178px"><svg><use href="#icon-mobile"/></svg>xx xxx xxx xxx</div>
  <div class="abs contact" style="left:660px;top:178px"><svg><use href="#icon-fax"/></svg>(925) xxx xxxx</div>
  <div class="abs contact" style="left:790px;top:178px"><svg><use href="#icon-mail"/></svg>xxxxx@email.com</div>
  <div class="abs contact" style="left:745px;top:204px">www.corvelmortgage.example</div>
</section>

<!-- Business card front -->
<section class="sheet card card-front" aria-label="Business card front">
  <div class="abs brand"><span class="brand-dot"></span>Brisvane Home Loans</div>
  <div class="abs person">
    <div class="person-name">Dale Whitcombe</div>
    <div class="person-title">President</div>
  </div>
  <div class="abs details">
    <div class="contact addr"><svg><use href="#icon-pin"/></svg><span>xxx xxxxx xxxxx<br>xxxxxxxxx, xxxxxx xxxxxx xxx</span></div>
    <div class="contact" style="margin-top:6px"><svg><use href="#icon-phone"/></svg>(xxx) xxx xxxx</div>
    <div class="contact"><svg><use href="#icon-mobile"/></svg>xx xxx xxx xxx</div>
    <div class="contact"><svg><use href="#icon-fax"/></svg>(xxx) xxx xxxx</div>
    <div class="contact"><svg><use href="#icon-mail"/></svg>xxxxxx@xxxxx.com</div>
  </div>
  <div class="abs front-rule"></div>
  <div class="abs front-band"></div>
</section>

<!-- Business card back -->
<section class="sheet card card-back" aria-label="Business card back">
  <div class="abs site">www.corvelmortgage.example</div>
  <div class="abs brand"><span class="brand-dot"></span>Brisvane Home Loans</div>
  <p class="abs message">Manifest your trust in us through the gift of your referrals.<br>We won't let you down.</p>
  <div class="abs back-rule"></div>
  <div class="abs back-band"></div>
</section>

<!-- Envelope -->
<section class="sheet envelope" aria-label="Envelope">
  <div class="abs brand"><span class="brand-dot"></span>Brisvane Home Loans</div>
  <div class="abs contact" style="left:175px;top:400px"><svg><use href="#icon-pin"/></svg>xxx xxxxxxx xxxxx</div>
  <div class="abs contact" style="left:190px;top:422px">xxxxxxxxx, xxxxxxxx xxxxx xxx</div>
  <div class="abs contact" style="left:385px;top:360px"><svg><use href="#icon-phone"/></svg>(xxx) xxx xxxx</div>
  <div class="abs contact" style="left:505px;top:360px"><svg><use href="#icon-mobile"/></svg>xx xxx xxx xxx</div>
  <div class="abs contact" style="left:625px;top:360px"><svg><use href="#icon-fax"/></svg>(925) xxx xxxx</div>
  <div class="abs contact" style="left:755px;top:350px"><svg><use href="#icon-mail"/></svg>xxxxx@email.com</div>
  <div class="abs contact" style="left:735px;top:374px">www.corvelmortgage.example</div>
  <div class="abs bottom-rule"></div>
  <div class="abs bottom-band"></div>
</section>

</body>
</html>
```